FOLI PACK FOR STICKS

Design the packaging for salted sticks (weight 400g) reference to the logo TOVEN (in attached).
Color packaging- look forward to suggestions.
Package with window.
Hi, we need only graphic conception without texts on back side.

Please find Logo TOVEN and the grid of packaging - attached
Updates

we need only graphic conception without texts on back side. Added Saturday, November 08, 2014

Target Market(s)

typical salted snack for everyone (adults and children included)

Font styles to use
Sans Serif

Requirements
Should not have
• - religion and politic signs…
• - toys and childdraws
• - monsters, devils and demons etc.

```html
<!DOCTYPE html>
<html lang="en">
<head>
<meta charset="utf-8">
<title>TOVEN Salted Sticks – Pack Front</title>
<link href="https://fonts.googleapis.com/css2?family=Nunito+Sans:wght@800&family=Lobster&display=swap" rel="stylesheet">
<style>
  :root {
    --backdrop: #efe9e0;
    --gold: #ecb73b;
    --gold-deep: #d9a12c;
    --cream: #fbeec8;
    --brown: #6b3d1e;
    --white: #ffffff;
    --bake-light: #f0cf9c;
    --bake-dark: #c98a4e;
  }
  * { margin: 0; padding: 0; box-sizing: border-box; }
  html, body { width: 1200px; height: 1000px; overflow: hidden; background: var(--backdrop); }
  .canvas { position: relative; width: 1200px; height: 1000px; }

  .pack {
    position: absolute; left: 415px; top: 150px; width: 372px; height: 700px;
    background: var(--gold);
    box-shadow: 0 6px 18px rgba(0,0,0,.18);
    overflow: hidden;
  }
  .cap-band { position: absolute; left: 0; width: 100%; height: 36px; background: var(--gold); }
  .cap-band.top { top: 0; }
  .cap-band.bottom { bottom: 0; height: 20px; }

  .stripe-band {
    position: absolute; left: 0; width: 100%;
    background: linear-gradient(90deg, var(--cream), var(--gold) 30%, var(--brown) 50%, var(--gold) 70%, var(--cream));
    opacity: .85;
  }
  .stripe-band.upper { top: 36px; height: 96px; }
  .stripe-band.lower { top: 592px; height: 88px; }

  .dot-rule {
    position: absolute; left: 0; width: 100%; height: 10px;
    background: var(--cream);
    border-top: 3px dotted var(--brown);
  }
  .dot-rule.r1 { top: 130px; }
  .dot-rule.r2 { top: 336px; }
  .dot-rule.r3 { top: 580px; }

  .title-panel {
    position: absolute; left: 0; top: 140px; width: 100%; height: 196px;
    background: var(--gold);
  }

  .brand-plate {
    position: absolute; left: 43px; top: 105px; width: 286px; height: 112px;
    background: var(--white); border-radius: 18px;
    border: 8px solid var(--gold-deep);
    display: flex; align-items: center; justify-content: center; gap: 12px;
  }
  .brand-dot { width: 18px; height: 18px; border-radius: 50%; background: var(--brown); }
  .brand-name {
    font-family: "Nunito Sans", Arial, sans-serif; font-weight: 800;
    font-size: 62px; letter-spacing: 1px; color: var(--brown); line-height: 1;
  }

  .product-name {
    position: absolute; left: 0; top: 258px; width: 100%; text-align: center;
    font-family: "Lobster", cursive; font-size: 44px; color: var(--brown);
    text-shadow: 2px 2px 0 var(--white), -2px -2px 0 var(--white), 2px -2px 0 var(--white), -2px 2px 0 var(--white);
  }

  .window {
    position: absolute; left: 0; top: 347px; width: 100%; height: 233px;
    background: linear-gradient(90deg, var(--bake-light), var(--bake-dark) 20%, var(--bake-light) 40%, var(--bake-dark) 60%, var(--bake-light) 80%, var(--bake-dark));
  }

  .quality-seal {
    position: absolute; left: 140px; top: 532px; width: 92px; height: 92px;
    border-radius: 50%; background: var(--cream);
    border: 5px solid var(--brown);
  }
</style>
</head>
<body>
<div class="canvas">
  <div class="pack">
    <div class="cap-band top"></div>
    <div class="stripe-band upper" role="img" aria-label="Vertical stripe pattern in brown, cream and gold"></div>
    <div class="dot-rule r1"></div>
    <div class="title-panel"></div>
    <div class="brand-plate">
      <span class="brand-dot"></span>
      <span class="brand-name">TOVEN</span>
    </div>
    <div class="product-name">Salted Sticks</div>
    <div class="dot-rule r2"></div>
    <div class="window" role="img" aria-label="Window showing baked sesame bread sticks"></div>
    <div class="dot-rule r3"></div>
    <div class="stripe-band lower" role="img" aria-label="Vertical stripe pattern in brown, cream and gold"></div>
    <div class="cap-band bottom"></div>
    <div class="quality-seal"></div>
  </div>
</div>
</body>
</html>
```